Business Card Design Project

Corvexa logo will be provided after
Front

Ned Marrowick- Construction Manager

Ph: (61) 07 53182079
nmarrowick@corvexa-example.com.au
PO Box 83 Kelvorin 4619

Back
Corvexa
EPCM

Oil - Gas - Mining

Industry/Entity Type

Business

Font styles to use
Sans Serif

Colors
faa54b

Requirements
Must have
• White Back Ground

```html
<!DOCTYPE html>
<html lang="en">
<head>
<meta charset="utf-8">
<title>Corvexa Business Card</title>
<link href="https://fonts.googleapis.com/css2?family=Arimo:wght@400;700&display=swap" rel="stylesheet">
<style>
  :root {
    --brand-orange: #f28c22;
    --ink: #1c1c1c;
    --paper: #ffffff;
    --backdrop: #dcdcdc;
  }
  * { box-sizing: border-box; margin: 0; padding: 0; }
  html, body {
    width: 1200px; height: 900px; overflow: hidden;
    background: var(--backdrop);
    font-family: "Arimo", Arial, sans-serif;
  }
  .canvas {
    width: 1200px; height: 900px;
    display: flex; flex-direction: column; align-items: center; justify-content: center;
    gap: 36px;
  }
  .card {
    position: relative;
    width: 700px; height: 400px;
    box-shadow: 0 6px 18px rgba(0,0,0,0.18);
    overflow: hidden;
  }

  /* Back side */
  .card-back { background: var(--paper); }
  .card-back .orange-field {
    position: absolute; left: 0; top: 0; width: 100%; height: 272px;
    background: var(--brand-orange);
    display: flex; align-items: center; justify-content: center;
  }
  .card-back .wordmark {
    color: var(--paper); font-weight: 700; font-size: 46px; letter-spacing: 3px;
    text-transform: uppercase;
  }
  .card-back .white-band {
    position: absolute; left: 0; top: 272px; width: 100%; height: 28px; background: var(--paper);
  }
  .card-back .orange-line {
    position: absolute; left: 0; top: 300px; width: 100%; height: 14px; background: var(--brand-orange);
  }
  .card-back .tagline {
    position: absolute; left: 0; top: 314px; width: 100%; height: 86px;
    display: flex; align-items: center; justify-content: space-between;
    padding: 0 60px; color: var(--brand-orange); font-size: 20px; word-spacing: 12px;
  }

  /* Front side */
  .card-front { background: var(--paper); }
  .card-front .wordmark {
    position: absolute; left: 46px; top: 150px;
    color: var(--ink); font-weight: 700; font-size: 56px; letter-spacing: 2px;
    text-transform: uppercase;
  }
  .card-front .name-plate {
    position: absolute; right: 0; top: 70px; width: 250px; height: 96px;
    background: var(--brand-orange); padding: 18px 22px;
    color: var(--ink);
  }
  .name-plate .person-name { font-weight: 700; font-size: 20px; margin-bottom: 8px; }
  .name-plate .person-role { font-size: 16px; }
  .card-front .contact {
    position: absolute; right: 40px; bottom: 34px;
    display: grid; grid-template-columns: auto auto; column-gap: 6px; row-gap: 8px;
    font-size: 16px; color: var(--ink);
  }
  .contact .label { color: var(--brand-orange); font-weight: 700; text-align: right; }
</style>
</head>
<body>
  <main class="canvas">
    <section class="card card-front" aria-label="Card front">
      <div class="wordmark">Corvexa</div>
      <div class="name-plate">
        <div class="person-name">Ned Marrowick</div>
        <div class="person-role">Construction Manager</div>
      </div>
      <div class="contact">
        <span class="label">Phone:</span><span>(61) 07 53182079</span>
        <span class="label">Web:</span><span>nmarrowick@corvexa-example.com.au</span>
        <span class="label">Address:</span><span>PO Box 83 Kelvorin 4619</span>
      </div>
    </section>

    <section class="card card-back" aria-label="Card back">
      <div class="orange-field"><div class="wordmark">Corvexa</div></div>
      <div class="white-band"></div>
      <div class="orange-line"></div>
      <div class="tagline">
        <span>Corvexa EPCM</span>
        <span>Oil Gas Mining</span>
      </div>
    </section>
  </main>
</body>
</html>
```